Lirevo Nocturna

Website for a night club with live music and cabaret dancers. I would like to have the following Menu: 1.) Home; 2) The Facilities; 3) The Show; 4) Other Attractions; 5) Videos & Fotos; 6) Program; 7) Reservations; 8) Membership; 9) Contacts.

The pages should be easily editable and allow to enter text, including the menu since the final version will be in both English and Portuguese. It should have a toggle or links for the Portuguese language and the English Language.

The night club itself is called "LIREVO NOCTURNA"; and its URL is www.lirevonocturna.example.

Industry/Entity Type

Night Club

```html
<!DOCTYPE html>
<html lang="en">
<head>
<meta charset="utf-8">
<title>Lirevo Nocturna</title>
<link rel="stylesheet" href="https://fonts.googleapis.com/css2?family=Source+Sans+3:ital,wght@0,400;0,600;0,700;1,400;1,700&display=swap">
<style>
  :root {
    --sky-top: #2c2260;
    --sky-mid: #5a3a78;
    --sunset: #c8642e;
    --sunset-glow: #e89a3a;
    --shore: #1c1218;
    --column: rgba(20, 14, 40, 0.45);
    --nav-gold: #d59a1a;
    --nav-active: #8c4a78;
    --nav-line: #7a3f6c;
    --frame: #b6a67c;
    --panel: #b1a37b;
    --ink: #2a2118;
    --heading: #7e3d72;
    --white: #ffffff;
    --photo-dark: #2a1e1e;
    --copyright: #9a8f9c;
  }
  html, body {
    margin: 0;
    padding: 0;
    width: 1200px;
    height: 1172px;
    overflow: hidden;
  }
  body {
    position: relative;
    font-family: "Source Sans 3", "Myriad Pro", sans-serif;
    background: var(--shore);
  }
  .scenery {
    position: absolute;
    inset: 0;
    background: linear-gradient(180deg, var(--sky-top) 0%, var(--sky-mid) 30%, #8a4a6a 45%, var(--sunset) 58%, var(--sunset-glow) 66%, #6a3a2a 80%, var(--shore) 100%);
  }
  .page-column {
    position: absolute;
    left: 67px;
    top: 0;
    width: 1067px;
    height: 1172px;
    background: var(--column);
  }
  .brand {
    position: absolute;
    left: 0;
    width: 1200px;
    top: 14px;
    text-align: center;
  }
  .brand-mark {
    display: block;
    margin: 0 auto;
  }
  .brand-name {
    margin: 10px 0 0;
    font-size: 36px;
    font-weight: 700;
    color: #c9a9d8;
    letter-spacing: 0.5px;
  }
  .languages {
    position: absolute;
    top: 183px;
    left: 1042px;
    display: flex;
    gap: 15px;
  }
  .languages a { display: block; line-height: 0; }
  .main-nav {
    position: absolute;
    left: 83px;
    top: 216px;
    width: 1038px;
    height: 36px;
    background: var(--nav-gold);
    border-bottom: 5px solid var(--nav-line);
    display: flex;
    flex-wrap: nowrap;
    justify-content: space-between;
    padding-right: 10px;
    box-sizing: content-box;
  }
  .main-nav a {
    color: var(--white);
    text-decoration: none;
    font-size: 17.5px;
    line-height: 36px;
    height: 36px;
    padding: 0 15px;
    white-space: nowrap;
    flex: 0 0 auto;
  }
  .main-nav a.is-active {
    background: var(--nav-active);
  }
  .promo-card {
    position: absolute;
    left: 83px;
    width: 333px;
    height: 178px;
    background: var(--frame);
    box-sizing: border-box;
    padding: 10px;
    box-shadow: 0 3px 8px rgba(0,0,0,0.5);
  }
  .promo-card.gallery { top: 273px; }
  .promo-card.party { top: 464px; }
  .promo-art {
    position: relative;
    width: 100%;
    height: 100%;
  }
  .gallery .promo-art { background: radial-gradient(ellipse at 62% 40%, #5a3a3a 0%, var(--photo-dark) 60%); }
  .party .promo-art { background: radial-gradient(ellipse at 52% 40%, #8a6a3a 0%, #4a2a5a 40%, var(--photo-dark) 75%); }
  .promo-label {
    position: absolute;
    left: 0;
    right: 0;
    bottom: 10px;
    text-align: center;
    color: var(--white);
    font-size: 23px;
    letter-spacing: 0.2px;
    white-space: nowrap;
  }
  .hero {
    position: absolute;
    left: 435px;
    top: 272px;
    width: 687px;
    height: 370px;
    background: var(--frame);
    padding: 12px;
    box-sizing: border-box;
    box-shadow: 0 3px 8px rgba(0,0,0,0.5);
  }
  .hero-photo {
    position: relative;
    width: 100%;
    height: 100%;
    background: linear-gradient(90deg, #3a2e2c 0%, #6a5a3a 20%, #b8b040 45%, #8a9a50 65%, #c8c4c8 92%, #d8d6da 100%);
  }
  .hero-caption {
    position: absolute;
    left: 10px;
    top: 244px;
    width: 424px;
    height: 96px;
    background: rgba(30, 24, 24, 0.78);
    color: var(--white);
    padding: 8px 10px;
    box-sizing: border-box;
  }
  .hero-caption h2 {
    margin: 0 0 2px;
    font-size: 29px;
    font-weight: 400;
    font-style: italic;
    line-height: 32px;
  }
  .hero-caption p {
    margin: 0;
    font-size: 16.5px;
    line-height: 22px;
    white-space: nowrap;
  }
  .content-panel {
    position: absolute;
    left: 435px;
    top: 660px;
    width: 687px;
    height: 477px;
    background: var(--panel);
    box-sizing: border-box;
    padding: 8px 24px 0 20px;
    box-shadow: 0 3px 8px rgba(0,0,0,0.5);
    color: var(--ink);
  }
  .content-panel h1 {
    margin: 0 0 4px;
    font-size: 33px;
    font-weight: 700;
    font-style: italic;
    color: var(--heading);
    text-shadow: 1px 1px 0 #4a2a44;
    line-height: 38px;
  }
  .content-panel p {
    margin: 0 0 23.5px;
    font-size: 16.8px;
    line-height: 23.7px;
    letter-spacing: -0.15px;
  }
  .copyright {
    position: absolute;
    left: 87px;
    top: 1143px;
    margin: 0;
    font-size: 13px;
    color: var(--copyright);
  }
</style>
</head>
<body>
  <div class="scenery" role="img" aria-label="Painted tropical sunset over the sea with silhouetted palm trees"></div>
  <div class="page-column"></div>

  <header class="brand">
    <svg class="brand-mark" width="106" height="106" viewBox="0 0 106 106" aria-hidden="true">
      <circle cx="53" cy="53" r="50" fill="#c78a1e"/>
    </svg>
    <p class="brand-name">Lirevo Nocturna</p>
  </header>

  <nav class="languages" aria-label="Language">
    <a href="#en" aria-label="English">
      <svg width="32" height="21" viewBox="0 0 32 21">
        <rect width="32" height="21" fill="#1f3a8a"/>
        <path d="M0 0 L32 21 M32 0 L0 21" stroke="#ffffff" stroke-width="4"/>
        <path d="M0 0 L32 21 M32 0 L0 21" stroke="#c8202e" stroke-width="1.5"/>
        <rect x="13" y="0" width="6" height="21" fill="#ffffff"/>
        <rect x="0" y="7.5" width="32" height="6" fill="#ffffff"/>
        <rect x="14.5" y="0" width="3" height="21" fill="#c8202e"/>
        <rect x="0" y="9" width="32" height="3" fill="#c8202e"/>
      </svg>
    </a>
    <a href="#pt" aria-label="Português">
      <svg width="32" height="21" viewBox="0 0 32 21">
        <rect width="13" height="21" fill="#1a7a2a"/>
        <rect x="13" width="19" height="21" fill="#d0201e"/>
        <circle cx="13" cy="10.5" r="4.5" fill="#f2c81e"/>
      </svg>
    </a>
  </nav>

  <nav class="main-nav" aria-label="Main">
    <a class="is-active" href="#home">Home</a>
    <a href="#facilities">Facilities</a>
    <a href="#show">Show</a>
    <a href="#attractions">Other Attractions</a>
    <a href="#media">Videos &amp; Fotos</a>
    <a href="#program">Program</a>
    <a href="#reservations">Reservations</a>
    <a href="#membership">Membership</a>
    <a href="#contacts">Contacts</a>
  </nav>

  <a class="promo-card gallery" href="#gallery">
    <div class="promo-art" role="img" aria-label="Photo of a photographer holding a camera">
      <span class="promo-label">LAST PARTY’S GALLERY</span>
    </div>
  </a>

  <a class="promo-card party" href="#party">
    <div class="promo-art" role="img" aria-label="Illustration of a dancing couple in front of palm leaves">
      <span class="promo-label">THE NEAREST PARTY</span>
    </div>
  </a>

  <section class="hero">
    <div class="hero-photo" role="img" aria-label="Photo of four cabaret dancers in colourful feathered costumes">
      <div class="hero-caption">
        <h2>Cabaret dancers</h2>
        <p>Any text about cabaret dancers. Any text about cabaret<br>Any text about cabaret dancers.dancers. Any text about</p>
      </div>
    </div>
  </section>

  <main class="content-panel">
    <h1>Home</h1>
    <p>Any text in home section. Any text in home section. Any text in home section. Any text in home section. Any text in home section. Any text in home section. Any text in home section. Any text in home section. Any text in home section.<br>Any text in home section. Any text in home section. Any text in home section. Any text in home section.</p>
    <p>Any text in home section. Any text in home section. Any text in home section. Any text in home section. Any text in home section. Any text in home section. Any text in home section.</p>
    <p>Any text in home section. Any text in home section. Any text in home section. Any text in home section. Any text in home section. Any text in home section. Any text in home section. Any text in home section.</p>
    <p>Any text in home section. Any text in home section.</p>
    <p>Any text in home section. Any text in home section. Any text in home section. Any text in home section. Any text in home section. Any text in home section. Any text in home section. Any text in home section. Any text in</p>
  </main>

  <p class="copyright">Copyright © 2014. All rights reserved.</p>
</body>
</html>
```